Standard logo business card

We are seeking a solid, somewhat understated professional design. We are a tech company. We like fonts similar to Aptifer Slab. Front side will be white with the contact information and a small version of our primary (Light background) logo.

(We have three people so we will have three names and titles)

Back side will hold our reverse logo on dark background along with the tagline:

"Intelligent annotation solutions for complex data"

Target Market(s)

Professionals, Tech

Industry/Entity Type

Business

Contact Information for Business Card

Name
Title

Phone
Email
City, State
Website

[We will email leading designer specific contact information)

Font styles to use
Serif

Requirements
Must have
• Colors are:
• Orange RGB 245,92,23
• Blue RGB 3,34,56
Nice to have
• We like a split with the Name and Title on the right and then contact details (below) on the left.

```html
<!DOCTYPE html>
<html lang="en">
<head>
<meta charset="utf-8">
<title>Northvane Business Card</title>
<link rel="stylesheet" href="https://fonts.googleapis.com/css2?family=Roboto+Slab:wght@400;700&display=swap">
<style>
  :root {
    --navy: #2a3140;
    --orange: #f0672e;
    --card-light: #f6f6f6;
    --card-mid: #e4e4e4;
    --band-grey: #d9dadc;
    --backdrop: #3a3633;
    --text-dark: #2a2d33;
    --text-light: #ffffff;
    --text-soft: #c9ced8;
  }
  * { box-sizing: border-box; margin: 0; padding: 0; }
  html, body {
    width: 1200px; height: 899px; overflow: hidden;
    background: var(--backdrop);
    font-family: "Roboto Slab", serif;
  }
  .stage { position: relative; width: 1200px; height: 899px; }
  .card {
    position: absolute; width: 700px; height: 400px; overflow: hidden;
    background: radial-gradient(ellipse at 40% 40%, var(--card-light) 0%, var(--card-mid) 100%);
    box-shadow: 0 14px 30px rgba(0,0,0,.45);
  }
  .card--back {
    left: 110px; top: 50px;
    background: radial-gradient(ellipse at 45% 40%, #343c4d 0%, var(--navy) 100%);
  }
  .card--front { left: 390px; top: 450px; }
  .card__art { position: absolute; inset: 0; }

  .wordmark {
    position: absolute; display: flex; align-items: center;
    color: var(--navy); font-weight: 700; letter-spacing: -1px; line-height: 1;
  }
  .wordmark__square { background: var(--orange); display: block; }
  .card--back .wordmark {
    left: 0; right: 0; top: 138px; justify-content: center;
    font-size: 72px; gap: 18px; color: var(--text-light);
  }
  .card--back .wordmark__square { width: 38px; height: 38px; }
  .tagline {
    position: absolute; left: 0; right: 0; top: 238px; text-align: center;
    color: var(--text-soft); font-size: 17px; letter-spacing: 1px;
  }
  .card--front .wordmark { left: 46px; top: 150px; font-size: 56px; gap: 14px; }
  .card--front .wordmark__square { width: 30px; height: 30px; }

  .identity {
    position: absolute; right: 36px; top: 104px; text-align: right; color: var(--text-light);
  }
  .identity__name { font-size: 20px; letter-spacing: 2px; font-weight: 400; }
  .identity__title { font-size: 15px; letter-spacing: 1px; margin-top: 4px; }

  .contact {
    position: absolute; left: 46px; top: 245px; list-style: none;
    color: var(--text-dark); font-size: 13px; letter-spacing: 1px;
  }
  .contact li { display: flex; align-items: center; gap: 10px; height: 23px; }
  .contact svg { width: 14px; height: 14px; fill: var(--text-dark); flex: none; }
  .contact__small { font-size: 12px; }
  .icon-line { fill: none !important; stroke: var(--text-dark); stroke-width: 1.4; }

  .address {
    position: absolute; right: 70px; bottom: 22px; text-align: right;
    color: var(--text-dark); font-size: 14px; letter-spacing: 1px; line-height: 1.5;
  }
</style>
</head>
<body>
<main class="stage">

  <section class="card card--back" aria-label="Card back">
    <div class="wordmark"><span class="wordmark__square"></span>northvane</div>
    <p class="tagline">Intelligent annotation solutions for complex data</p>
  </section>

  <section class="card card--front" aria-label="Card front">
    <svg class="card__art" viewBox="0 0 700 400" aria-hidden="true">
      <path fill="var(--band-grey)" d="M0,82 C330,38 600,110 700,300 L700,400 L690,400 C620,170 360,60 0,90 Z"/>
      <path fill="var(--orange)" d="M0,78 C330,36 600,106 700,282 L700,372 C610,150 340,46 0,82 Z"/>
      <path fill="var(--navy)" d="M0,0 H700 V282 C600,106 330,36 0,74 Z"/>
    </svg>

    <div class="identity">
      <p class="identity__name">DANIEL MERCER</p>
      <p class="identity__title">Managing Director</p>
    </div>

    <div class="wordmark"><span class="wordmark__square"></span>northvane</div>

    <ul class="contact">
      <li><svg viewBox="0 0 16 16"><path d="M4 1l3 3-2 2c1 2 3 4 5 5l2-2 3 3-2 3C7 15 1 9 1 3z"/></svg>014 552 7310</li>
      <li><svg viewBox="0 0 16 16"><path d="M4 0h8v16H4z M5 2v11h6V2z"/></svg>014 552 7310</li>
      <li><svg viewBox="0 0 16 16"><path d="M1 6h3V1h8v5h3v9H1z M5 2v4h6V2z M3 9h2v2H3z M7 9h2v2H7z M11 9h2v2h-2z"/></svg>014 552 7310</li>
      <li class="contact__small"><svg viewBox="0 0 16 16"><path d="M0 3h16v10H0z"/></svg>hello@northvane.com</li>
      <li class="contact__small"><svg viewBox="0 0 16 16"><g class="icon-line"><circle cx="8" cy="8" r="7"/><ellipse cx="8" cy="8" rx="3" ry="7"/><path d="M1 8h14"/></g></svg>www.northvane.com</li>
    </ul>

    <p class="address">041.12th floor,Arden<br>Kestrel Road NVL</p>
  </section>

</main>
</body>
</html>
```